依頼詳細
ポスティングを行いますので、そのためのチラシを作製頂きたいと思います。

①一見して業態が伝わるようなデザインにして頂けるとありがたいです。文字だけでなく、イラスト等も入れてキャッチ―な感じにして下さい。

②1回限り、10km圏内の出張費を無料にするという内容のチケットを組み込んで下さい。

③使用して頂きたい文言の例は以下の通りです。(あくまでも例ですので、適宜変更・追加して頂いても問題ございません。)
・パソコンのことなら何でもご相談下さい
・診断やお見積もりは無料です
・自社内修理なので迅速対応
・ご予算や用途に合わせたBTO PCも販売

④相談してもらいたい困り事の例は以下の通りです。(必ずしも全て入れて頂く必要はありません。)
・パソコンの動作が遅い
・突然起動しなくなった
・ネットに繋がらない
・設定方法がわからない
・操作方法を教えて欲しい
・ウイルスに感染したかもしれない
・突然電源が落ちたりフリーズする
・画面が映らない
・黒い画面に英語のメッセージが表示される

記載項目
屋号:PC NEXLO(ピーシーネクスロ)
住所:気仙沼市北瀬32-4 モルタナとなり
電話・FAX共通:0226-48-3071
営業時間:10時~21時 年中無休
メール:pcnexlo@vqt-net.com
Web:www.vqt-net.com
支払い:クレジットカード利用可
その他:所在地略図
サイズ
B4
ページ数
片面
希望イメージ
シンプル 複雑
単色 カラフル
暗い 明るい
日常 高級
遊び心 厳粛
未来的 伝統的
女性的 男性的
希望する色
青系
納品ファイル
• イラストレーター形式 (.ai)
補足説明
作製に当たって不足している情報等がありましたら、メッセージにてご連絡を頂けましたら幸いです。
多数の皆様から様々なご提案を頂き、誠にありがとうございました。改めて御礼
申し上げます。

力作揃いで非常に悩ましいところではございますが、出来るだけ早く最終的な選定
を行わせて頂きたいと存じます。

本来であれば、お一方ずつ御礼を述べさせて頂きたいところではございますが、とり
急ぎ本欄より失礼致します。引き続き宜しくお願い申し上げます。
■ 選んだ理由

ご提案頂いた際、サムネイル画像を見ただけでもインパクトがあり、訴求したい要件も非常にうまくまとめられておりました。当方では気付かないような細かい点までご配慮頂くなど、要望以上のご提案を頂くことが出来ました。改めて御礼申し上げます。

■ 提案者全員のお礼・コメント

この度は多くのランサー様から多数の力作をご提案頂き、本当にありがとうございました。何れの作品も素晴らしく、選定も非常に難航致しました。今後も定期的に案件をお願いする機会があると思いますので、その際もご提案賜れましたら幸いです。今後とも宜しくお願い申し上げます。

```html
<!DOCTYPE html>
<html lang="ja">
<head>
<meta charset="utf-8">
<title>PC NEXLO チラシ</title>
<link href="https://fonts.googleapis.com/css2?family=Noto+Sans+JP:wght@400;500;700;900&display=swap" rel="stylesheet">
<style>
:root{
  --blue:#1a7fd0;
  --blue-deep:#0d4f9a;
  --navy:#12306b;
  --sky:#d9ecfa;
  --red:#e2262b;
  --orange:#f08a00;
  --yellow:#ffe33b;
  --ink:#222;
  --white:#fff;
  --paper:#f6fafd;
}
*{box-sizing:border-box;margin:0;padding:0}
html,body{width:849px;height:1200px;overflow:hidden}
body{font-family:"Noto Sans JP",sans-serif;color:var(--ink);background:var(--white)}
.flyer{position:relative;width:849px;height:1200px;overflow:hidden;background:var(--white)}
.hero-photo{position:absolute;left:0;top:0;width:849px;height:420px;
  background:linear-gradient(160deg,#f3f5f7 0%,#dfe6ec 45%,#c9d4de 100%)}
.badge-quick{position:absolute;left:36px;top:36px;width:200px;padding:14px 10px;background:var(--white);
  border:3px solid var(--blue);text-align:center;border-radius:4px}
.badge-quick .small{font-size:20px;font-weight:700;color:var(--blue-deep)}
.badge-quick .big{font-size:38px;font-weight:900;color:var(--red);line-height:1.15}
.badge-quick .tag{display:inline-block;margin-top:6px;background:var(--red);color:var(--white);
  font-size:16px;font-weight:700;padding:2px 12px}
.bubble{position:absolute;left:330px;top:195px;width:260px;padding:14px 12px;background:var(--white);
  border:3px solid var(--red);border-radius:40px;text-align:center;line-height:1.3}
.bubble .l1{font-size:22px;font-weight:700;color:var(--ink)}
.bubble .l2{font-size:30px;font-weight:900;color:var(--red)}
.bubble svg{position:absolute;right:-26px;top:30px}
.band{position:absolute;left:0;top:400px;width:849px;height:220px}
.headline{position:absolute;left:36px;top:438px;color:var(--white);font-weight:900;line-height:1.2;
  text-shadow:0 3px 0 var(--navy)}
.headline .h1{font-size:64px;letter-spacing:1px}
.headline .h2{font-size:70px;letter-spacing:1px}
.headline .h2 em{font-style:normal;color:var(--yellow);font-size:88px}
.consult{position:absolute;left:604px;top:465px;font-size:28px;font-weight:900;color:var(--navy);line-height:1.3}
.trouble-title{position:absolute;left:36px;top:630px;font-size:34px;font-weight:900;color:var(--navy)}
.checklist{position:absolute;left:36px;top:688px;width:450px;list-style:none;
  display:grid;grid-template-columns:1fr 1fr;row-gap:6px;column-gap:8px}
.checklist li{display:flex;align-items:center;gap:6px;font-size:16px;font-weight:700;white-space:nowrap;
  border-bottom:1px dotted #9bb;padding-bottom:5px}
.checklist li.wide{grid-column:1 / 3}
.checklist svg{flex:none}
.shop-photo{position:absolute;left:600px;top:640px;width:230px;height:130px;
  background:linear-gradient(180deg,#cfe2f3 0%,#e9eef2 55%,#b7c0c8 100%)}
.coupon-badge{position:absolute;left:488px;top:730px;width:110px;height:110px;border-radius:50%;
  background:var(--blue);border:4px solid var(--white);color:var(--white);text-align:center;
  display:flex;flex-direction:column;justify-content:center;line-height:1.2}
.coupon-badge .s{font-size:13px;font-weight:700}
.coupon-badge .b{font-size:20px;font-weight:900;color:var(--yellow)}
.brand{position:absolute;left:606px;top:778px;width:230px}
.brand .kana{font-size:14px;font-weight:700;color:var(--navy)}
.brand .name{display:flex;align-items:center;gap:8px;margin-top:2px;font-size:34px;font-weight:900;color:var(--blue-deep);line-height:1.3}
.brand .name i{display:block;width:24px;height:24px;background:var(--blue-deep)}
.brand .info{margin-top:4px;font-size:12px;font-weight:500;line-height:1.55}
.brand .fax{margin-top:2px;font-size:16px;font-weight:900;color:var(--navy)}
.tel-box{position:absolute;left:440px;top:936px;width:390px;height:54px;background:var(--orange);
  color:var(--white);display:flex;align-items:center;justify-content:center;gap:10px;
  font-size:40px;font-weight:900;letter-spacing:1px}
.address{position:absolute;left:440px;top:994px;width:390px;font-size:13px;text-align:center;font-weight:500}
.bto{position:absolute;left:36px;top:940px;width:390px;background:var(--blue);color:var(--white);
  padding:8px 14px;line-height:1.25}
.bto .s{font-size:16px;font-weight:700}
.bto .b{font-size:30px;font-weight:900}
.bto .b span{color:var(--yellow)}
.contact-line{position:absolute;left:36px;display:flex;align-items:center;gap:10px;font-size:22px;font-weight:700;color:var(--navy)}
.map{position:absolute;left:36px;top:1098px;width:390px;height:90px;background:#e3e6e8;
  border:1px solid #b5bcc2;display:flex;align-items:center;justify-content:center;font-size:16px;color:#555}
.ticket{position:absolute;left:440px;top:1020px;width:390px;height:168px;border:3px dashed var(--blue);
  background:var(--paper);text-align:center;padding-top:22px}
.ticket .t{font-size:46px;font-weight:900;color:var(--red);letter-spacing:4px}
.ticket .n{margin-top:8px;font-size:17px;font-weight:700;color:var(--navy)}
.ticket .note{margin-top:4px;font-size:13px;color:#444}
</style>
</head>
<body>
<div class="flyer">
  <div class="hero-photo" role="img" aria-label="ノートパソコンと立体のQ&A文字、パソコンを操作するスタッフの写真"></div>

  <div class="badge-quick">
    <div class="small">自社内修理で</div>
    <div class="big">迅速対応</div>
    <div class="tag">年中無休</div>
  </div>

  <div class="bubble">
    <div class="l1">パソコンの</div>
    <div class="l2">診断や見積りが無料!</div>
    <svg width="30" height="30" viewBox="0 0 30 30"><path d="M0 4 L28 14 L0 24 Z" fill="#fff" stroke="#e2262b" stroke-width="3"/></svg>
  </div>

  <svg class="band" viewBox="0 0 849 220" preserveAspectRatio="none">
    <polygon points="0,20 590,0 570,200 0,220" fill="#1a7fd0"/>
    <polygon points="590,0 849,30 849,200 570,200" fill="#d9ecfa"/>
  </svg>
  <div class="headline">
    <div class="h1">パソコンの困った</div>
    <div class="h2">すべて<em>解決!</em></div>
  </div>
  <div class="consult">パソコンの<br>ことなら何でも<br>ご相談下さい</div>

  <div class="trouble-title">こんなお困りありませんか?</div>
  <ul class="checklist">
    <li><svg width="22" height="22" viewBox="0 0 22 22"><rect x="1" y="1" width="20" height="20" fill="#fff" stroke="#e2262b" stroke-width="2"/><path d="M5 11 L9 16 L17 5" fill="none" stroke="#e2262b" stroke-width="3"/></svg>パソコンの動作が遅い</li>
    <li><svg width="22" height="22" viewBox="0 0 22 22"><rect x="1" y="1" width="20" height="20" fill="#fff" stroke="#e2262b" stroke-width="2"/><path d="M5 11 L9 16 L17 5" fill="none" stroke="#e2262b" stroke-width="3"/></svg>突然起動しなくなった</li>
    <li><svg width="22" height="22" viewBox="0 0 22 22"><rect x="1" y="1" width="20" height="20" fill="#fff" stroke="#e2262b" stroke-width="2"/><path d="M5 11 L9 16 L17 5" fill="none" stroke="#e2262b" stroke-width="3"/></svg>ネットに繋がらない</li>
    <li><svg width="22" height="22" viewBox="0 0 22 22"><rect x="1" y="1" width="20" height="20" fill="#fff" stroke="#e2262b" stroke-width="2"/><path d="M5 11 L9 16 L17 5" fill="none" stroke="#e2262b" stroke-width="3"/></svg>設定方法がわからない</li>
    <li><svg width="22" height="22" viewBox="0 0 22 22"><rect x="1" y="1" width="20" height="20" fill="#fff" stroke="#e2262b" stroke-width="2"/><path d="M5 11 L9 16 L17 5" fill="none" stroke="#e2262b" stroke-width="3"/></svg>操作方法を教えて欲しい</li>
    <li><svg width="22" height="22" viewBox="0 0 22 22"><rect x="1" y="1" width="20" height="20" fill="#fff" stroke="#e2262b" stroke-width="2"/><path d="M5 11 L9 16 L17 5" fill="none" stroke="#e2262b" stroke-width="3"/></svg>画面が映らない</li>
    <li class="wide"><svg width="22" height="22" viewBox="0 0 22 22"><rect x="1" y="1" width="20" height="20" fill="#fff" stroke="#e2262b" stroke-width="2"/><path d="M5 11 L9 16 L17 5" fill="none" stroke="#e2262b" stroke-width="3"/></svg>ウイルスに感染したかもしれない</li>
    <li class="wide"><svg width="22" height="22" viewBox="0 0 22 22"><rect x="1" y="1" width="20" height="20" fill="#fff" stroke="#e2262b" stroke-width="2"/><path d="M5 11 L9 16 L17 5" fill="none" stroke="#e2262b" stroke-width="3"/></svg>突然電源が落ちたりフリーズする</li>
    <li class="wide"><svg width="22" height="22" viewBox="0 0 22 22"><rect x="1" y="1" width="20" height="20" fill="#fff" stroke="#e2262b" stroke-width="2"/><path d="M5 11 L9 16 L17 5" fill="none" stroke="#e2262b" stroke-width="3"/></svg>黒い画面に英語のメッセージが表示される</li>
  </ul>

  <div class="shop-photo" role="img" aria-label="店舗外観の写真"></div>
  <div class="coupon-badge">
    <div class="s">今だけ特典<br>サービス券</div>
    <div class="b">出張費<br>無料</div>
  </div>

  <div class="brand">
    <div class="kana">PC NEXLO(ピーシーネクスロ)</div>
    <div class="name"><i></i>PC NEXLO</div>
    <div class="info">●営業時間/10時~21時 年中無休<br>●クレジットカード利用可</div>
    <div class="fax">TEL/FAX共通</div>
  </div>

  <div class="tel-box">
    <svg width="34" height="34" viewBox="0 0 24 24"><path d="M6.6 10.8a15 15 0 0 0 6.6 6.6l2.2-2.2a1 1 0 0 1 1-.25 11.4 11.4 0 0 0 3.6.57 1 1 0 0 1 1 1V20a1 1 0 0 1-1 1A17 17 0 0 1 3 4a1 1 0 0 1 1-1h3.5a1 1 0 0 1 1 1c0 1.25.2 2.45.57 3.6a1 1 0 0 1-.25 1z" fill="#fff"/></svg>
    0226-48-3071
  </div>
  <div class="address">〒988-0071 宮城県気仙沼市北瀬32-4 モルタナとなり</div>

  <div class="bto">
    <div class="s">ご予算や用途に合わせカスタマイズ</div>
    <div class="b"><span>BTO PC</span>も販売中</div>
  </div>
  <div class="contact-line" style="top:1018px">
    <svg width="28" height="28" viewBox="0 0 28 28"><rect width="28" height="28" rx="4" fill="#1a7fd0"/><circle cx="14" cy="14" r="8" fill="none" stroke="#fff" stroke-width="2"/><path d="M6 14h16M14 6c-4 4-4 12 0 16M14 6c4 4 4 12 0 16" fill="none" stroke="#fff" stroke-width="1.5"/></svg>
    www.vqt-net.com
  </div>
  <div class="contact-line" style="top:1056px">
    <svg width="28" height="28" viewBox="0 0 28 28"><rect width="28" height="28" rx="4" fill="#1a7fd0"/><rect x="6" y="8" width="16" height="12" fill="none" stroke="#fff" stroke-width="2"/><path d="M6 8l8 7 8-7" fill="none" stroke="#fff" stroke-width="2"/></svg>
    pcnexlo@vqt-net.com
  </div>
  <div class="map" role="img" aria-label="所在地略図">MAP</div>

  <div class="ticket">
    <div class="t">出張費無料券</div>
    <div class="n">対応エリア10km圏内 1回限り有効</div>
    <div class="note">ご依頼の際に本券をご提示ください</div>
  </div>
</div>
</body>
</html>
```